Home Improvement Company in need of a "Banner & Billboard Design"

I'm Looking for a Banner design 4X6 With Company Logo, Phone Number, website, Credentials and services.. I picture a charcoal/matte background i also want to look like a house shape design i will upload the sample...

I'm looking for a Billboard design to target homeowners who need Roofing Services. I need logo, number, website, KTL, Credentials and a catchy title. i will like to use the same colors for branding

Target Market(s)

Homeowners, Investors,

Industry/Entity Type

Home Improvement

Font styles to use
Decorative

Colors
00a990
5c5c5c
333333

Requirements
Must have
• All Credentials, Phone number, website, logo, logo colors, services, Eye Catchy, Direct Message, Friendly feeling,
• (614) 372 - 9058
• Roofing Gutters Painting Pressure Washing Exterior Design
Nice to have
• A catchy title, A direct message to a homeowner looking for home improvement services. noticeable
Should not have
• not Busy, no

```html
<!DOCTYPE html>
<html lang="en">
<head>
<meta charset="utf-8">
<title>Crestline Home Exteriors – Banner</title>
<link rel="stylesheet" href="https://fonts.googleapis.com/css2?family=Roboto+Condensed:wght@400;500;700&display=swap">
<style>
  :root {
    --teal: #00a990;
    --charcoal: #333333;
    --slate: #5c5c5c;
    --white: #ffffff;
    --bullet: #8a8a8a;
  }
  * { margin: 0; padding: 0; box-sizing: border-box; }
  html, body { width: 800px; height: 1200px; overflow: hidden; background: var(--white); }
  .banner {
    position: relative; width: 800px; height: 1200px; overflow: hidden;
    background: var(--white);
    font-family: "Roboto Condensed", "Arial Narrow", sans-serif;
  }
  .backdrop {
    position: absolute; left: 0; top: 440px; width: 800px; height: 650px;
    background: linear-gradient(160deg, var(--teal) 0%, var(--charcoal) 48%, var(--charcoal) 100%);
  }

  .brand {
    position: absolute; left: 66px; top: 150px; width: 470px;
    color: var(--teal); font-weight: 700; text-transform: uppercase; text-align: center;
  }
  .brand-name { display: block; font-size: 118px; line-height: 1; letter-spacing: 2px; }
  .brand-sub { display: block; font-size: 55px; line-height: 1.1; letter-spacing: 1px; margin-top: 14px; }

  .services {
    position: absolute; left: 0; top: 470px; width: 800px; list-style: none;
    color: var(--white); font-size: 36px; font-weight: 500;
  }
  .services li { position: absolute; white-space: nowrap; }
  .services li::before {
    content: ""; display: inline-block; width: 13px; height: 13px; border-radius: 50%;
    background: var(--bullet); margin-right: 16px; vertical-align: middle;
    position: relative; top: -3px;
  }

  .phone {
    position: absolute; right: 12px; top: 856px;
    color: var(--white); font-size: 88px; font-weight: 500; letter-spacing: 1px; white-space: nowrap;
  }
  .web-bar { position: absolute; left: 0; top: 962px; width: 800px; height: 60px; }
  .website {
    position: absolute; left: 180px; top: 962px; width: 620px; height: 60px;
    line-height: 60px; text-align: center;
    color: var(--charcoal); font-size: 50px; font-weight: 700; white-space: nowrap;
  }
  .licenses {
    position: absolute; left: 220px; top: 1032px;
    color: var(--white); font-size: 34px; font-weight: 700; white-space: nowrap;
  }
  .licenses span + span { margin-left: 28px; }

  .credentials { position: absolute; left: 0; top: 1090px; width: 800px; height: 110px; }
  .badge { position: absolute; }
  .badge-accredited { left: 161px; top: 8px; width: 56px; height: 92px; background: #1d5f9a; border-radius: 4px; }
  .badge-supplier { left: 294px; top: 14px; width: 78px; height: 78px; background: #d8262b; }
  .badge-certified { left: 452px; top: 16px; width: 190px; height: 66px; background: #d8262b; border-radius: 3px; }
</style>
</head>
<body>
<main class="banner">
  <div class="backdrop" role="img" aria-label="Layered teal and charcoal wave backdrop"></div>
  <svg class="web-bar" viewBox="0 0 800 60" aria-hidden="true">
    <path fill="var(--teal)" d="M188,0 L800,0 L800,60 L164,60 Z"/>
  </svg>

  <h1 class="brand">
    <span class="brand-name">Crestline</span>
    <span class="brand-sub">Home Exteriors</span>
  </h1>

  <ul class="services">
    <li style="left:598px; top:0;">Roofing</li>
    <li style="left:553px; top:58px;">Gutters</li>
    <li style="left:513px; top:118px;">Painting</li>
    <li style="left:466px; top:185px;">Pressure Washing</li>
    <li style="left:410px; top:252px;">Exterior Design</li>
  </ul>

  <p class="phone">(614) 372 - 9058</p>
  <p class="website">www.CrestlineExteriors.com</p>
  <p class="licenses"><span>OR #384512</span><span>WA #CRESTHE47310</span></p>

  <div class="credentials">
    <div class="badge badge-accredited" role="img" aria-label="Accreditation badge"></div>
    <div class="badge badge-supplier" role="img" aria-label="Roofing supplier badge"></div>
    <div class="badge badge-certified" role="img" aria-label="Certified contractor badge"></div>
  </div>
</main>
</body>
</html>
```